Small company security and risk consulting startup needs an explosive message via marketing colla...

Need a two page (front/back) flyer that calls out our three primary service areas incorporating brandmill developed logo and website visuals. Something that grabs attention at first glance to entice the viewer to read and connect for a services consultation. I will need the ability to make minor adjustments and add language.

```html
<!DOCTYPE html>
<html lang="en">
<head>
<meta charset="utf-8">
<title>Sentinel Ridge Consulting Services – Flyer Front and Back</title>
<link rel="stylesheet" href="https://fonts.googleapis.com/css2?family=Rajdhani:wght@600;700&family=Montserrat:wght@400;500;600;700&family=Roboto+Slab:wght@300&display=swap">
<style>
:root{
  --stage:#3d3d3d;
  --ink:#141414;
  --ink-soft:#262626;
  --red:#e0101c;
  --red-deep:#8e0a12;
  --blue:#0d3a9a;
  --blue-deep:#08246a;
  --white:#ffffff;
  --paper-grey:#e6e6e6;
  --text:#222222;
  --silver:#d9d9d9;
}
*{box-sizing:border-box;margin:0;padding:0}
html,body{width:1200px;height:863px;overflow:hidden;background:var(--stage)}
.stage{position:relative;width:1200px;height:863px}
.sheet{position:absolute;top:58px;width:508px;height:720px;overflow:hidden;background:var(--ink)}
.sheet--front{left:66px}
.sheet--back{left:630px;background:var(--white)}
.sheet-label{position:absolute;top:802px;font:300 22px/1 "Roboto Slab",serif;letter-spacing:6px;color:#e8e8e8}
.abs{position:absolute}
.brand{position:absolute;left:0;width:508px;text-align:center;color:var(--white)}
.brand-dot{display:block;margin:0 auto;width:40px;height:40px;border-radius:50%;background:var(--red)}
.brand-name{font:700 28px/28px "Rajdhani",sans-serif;color:var(--silver);letter-spacing:1px}
.brand-sub{font:600 9.5px/1 "Montserrat",sans-serif;letter-spacing:5.5px;margin-top:4px}
.brand-tag{font:500 6.5px/1 "Montserrat",sans-serif;letter-spacing:3px;color:var(--red);margin-top:5px}
.headline{position:absolute;left:0;width:508px;text-align:center;color:var(--white);font:700 37px/37px "Rajdhani",sans-serif;letter-spacing:.5px}
.lede{position:absolute;left:40px;width:428px;text-align:center;color:#e6e6e6;font:400 10.6px/14px "Montserrat",sans-serif}
.footer{position:absolute;left:0;bottom:0;width:508px;height:64px}
.footer-call{position:absolute;left:46px;top:10px;font:700 10.5px/1 "Montserrat",sans-serif;color:var(--white)}
.footer-phone{position:absolute;left:43px;top:22px;font:700 31px/1 "Rajdhani",sans-serif;color:var(--white);letter-spacing:.5px}
.footer-contact{position:absolute;left:322px;font:500 14.5px/1 "Montserrat",sans-serif;color:var(--white)}
.section-title{position:absolute;left:30px;font:700 21px/1 "Rajdhani",sans-serif;color:var(--ink-soft)}
.section-title .accent{color:var(--red)}
.rule{position:absolute;left:30px;width:50px;height:1px;background:var(--ink-soft)}
.copy-block{position:absolute;left:30px;display:flex;flex-direction:column;gap:7px}
.copy{color:var(--text);font:400 9.3px/13px "Montserrat",sans-serif}
.copy--abs{position:absolute;left:30px}
.service{position:absolute;width:130px;text-align:center;color:var(--white)}
.service-title{font:700 10.5px/13.5px "Montserrat",sans-serif}
.service-text{font:400 7.6px/10px "Montserrat",sans-serif;color:rgba(255,255,255,.6);margin-top:6px}
.service--blue .service-text{color:rgba(255,255,255,.85)}
</style>
</head>
<body>
<div class="stage">

  <!-- FRONT -->
  <section class="sheet sheet--front">
    <svg class="abs" width="508" height="720" viewBox="0 0 508 720" style="left:0;top:0">
      <defs>
        <radialGradient id="heroGlow" cx="0.4" cy="0.4" r="0.8">
          <stop offset="0" stop-color="#2a8fd6"/>
          <stop offset="0.5" stop-color="#0d4a86"/>
          <stop offset="1" stop-color="#0a1f3a"/>
        </radialGradient>
        <radialGradient id="hexGlow" cx="0.5" cy="0.4" r="0.7">
          <stop offset="0" stop-color="#2a0a0c"/>
          <stop offset="1" stop-color="#0d0d0d"/>
        </radialGradient>
        <linearGradient id="callRed" x1="0" y1="0" x2="1" y2="1">
          <stop offset="0" stop-color="#e8141f"/>
          <stop offset="1" stop-color="#a80c15"/>
        </linearGradient>
      </defs>
      <rect role="img" aria-label="Photo of a hand tapping a tablet with glowing padlock, cloud, wifi and cart security icons" width="508" height="420" fill="url(#heroGlow)"/>
      <rect role="img" aria-label="Dark hexagon pattern with red glowing edges" y="350" width="508" height="370" fill="url(#hexGlow)"/>
      <polygon points="0,395 252,350 508,395 508,400 252,356 0,400" fill="var(--red)"/>
      <polygon points="0,400 252,356 508,400 508,410 0,410" fill="#111"/>
      <polygon points="0,656 273,656 262,720 0,720" fill="url(#callRed)"/>
      <polygon points="279,656 508,656 508,720 268,720" fill="#101010"/>
      <rect x="18" y="673" width="16" height="30" rx="3" fill="none" stroke="#fff" stroke-width="3"/>
      <rect x="22" y="697" width="8" height="3" fill="#fff"/>
      <rect x="300" y="666" width="11" height="8" fill="var(--red)"/>
      <polyline points="300,666 305.5,671 311,666" fill="none" stroke="#101010" stroke-width="1"/>
      <circle cx="305.5" cy="698" r="5.5" fill="none" stroke="var(--red)" stroke-width="1.2"/>
      <line x1="300" y1="698" x2="311" y2="698" stroke="var(--red)" stroke-width="1"/>
      <ellipse cx="305.5" cy="698" rx="2.3" ry="5.5" fill="none" stroke="var(--red)" stroke-width="1"/>
    </svg>

    <div class="brand" style="top:375px">
      <span class="brand-dot"></span>
      <div class="brand-name" style="margin-top:34px">Sentinel Ridge</div>
      <div class="brand-sub">CONSULTING SERVICES</div>
      <div class="brand-tag">commitment - integrity - results</div>
    </div>

    <h1 class="headline" style="top:518px">LOREM IPSUM<br>SIMPLY DUMMY TEXT</h1>
    <p class="lede" style="top:606px">Lorem Ipsum is simply dummy text of the printing and typesetting industry. Lorem Ipsum has been the industry's standard dummy text ever since the 1500s,</p>

    <div class="footer">
      <div class="footer-call">For More Information, Call Us Today!</div>
      <div class="footer-phone">0123.456.789</div>
      <div class="footer-contact" style="top:12px">info@yourmailid.com</div>
      <div class="footer-contact" style="top:34px">www.yourwebsite.com</div>
    </div>
  </section>

  <!-- BACK -->
  <section class="sheet sheet--back">
    <svg class="abs" width="508" height="720" viewBox="0 0 508 720" style="left:0;top:0">
      <defs>
        <radialGradient id="hexGlowBack" cx="0.5" cy="0.3" r="0.8">
          <stop offset="0" stop-color="#2a0a0c"/>
          <stop offset="1" stop-color="#0d0d0d"/>
        </radialGradient>
        <linearGradient id="photoTone" x1="0" y1="0" x2="1" y2="1">
          <stop offset="0" stop-color="#1a1a1a"/>
          <stop offset="0.6" stop-color="#4a4a4a"/>
          <stop offset="1" stop-color="#2b2b2b"/>
        </linearGradient>
        <linearGradient id="darkCard" x1="0" y1="0" x2="0" y2="1">
          <stop offset="0" stop-color="#202020"/>
          <stop offset="1" stop-color="#3a3a3a"/>
        </linearGradient>
        <linearGradient id="redCard" x1="0" y1="0" x2="0" y2="1">
          <stop offset="0" stop-color="#e0101c"/>
          <stop offset="1" stop-color="#6e0810"/>
        </linearGradient>
        <linearGradient id="blueCard" x1="0" y1="0" x2="0" y2="1">
          <stop offset="0" stop-color="#08246a"/>
          <stop offset="1" stop-color="#0d46b0"/>
        </linearGradient>
        <linearGradient id="callRedBack" x1="0" y1="0" x2="1" y2="1">
          <stop offset="0" stop-color="#e8141f"/>
          <stop offset="1" stop-color="#a80c15"/>
        </linearGradient>
      </defs>
      <polygon role="img" aria-label="Dark hexagon pattern with red glowing edges" points="0,0 508,0 508,91 251,137 0,91" fill="url(#hexGlowBack)"/>
      <polygon points="0,91 251,137 508,91 508,98 251,144 0,98" fill="var(--red)"/>
      <rect y="289" width="508" height="186" fill="var(--paper-grey)"/>
      <polygon role="img" aria-label="Black and white photo of a consultant presenting to a seated audience" points="245,475 400,289 508,289 508,475" fill="url(#photoTone)"/>
      <rect y="475" width="508" height="181" fill="#f3f3f3"/>
      <polygon points="0,545 52,478 150,478 203,570 178,651 0,651" fill="url(#darkCard)"/>
      <polygon points="127,478 367,478 284,651 225,651 175,570" fill="url(#redCard)"/>
      <polygon points="382,478 443,478 508,560 508,651 282,651" fill="url(#blueCard)"/>
      <polygon points="0,656 273,656 262,720 0,720" fill="url(#callRedBack)"/>
      <polygon points="279,656 508,656 508,720 268,720" fill="#101010"/>
      <g fill="none" stroke="#fff" stroke-width="1.4">
        <rect x="67" y="507" width="36" height="24" rx="1"/>
        <line x1="85" y1="531" x2="85" y2="537"/><line x1="78" y1="537" x2="92" y2="537"/>
        <ellipse cx="85" cy="519" rx="9" ry="5"/><circle cx="85" cy="519" r="2"/>
        <circle cx="254" cy="520" r="13"/><circle cx="254" cy="520" r="5"/>
        <line x1="254" y1="503" x2="254" y2="508"/><line x1="254" y1="532" x2="254" y2="537"/>
        <line x1="237" y1="520" x2="242" y2="520"/><line x1="266" y1="520" x2="271" y2="520"/>
        <rect x="400" y="505" width="22" height="14"/><rect x="410" y="512" width="22" height="14"/>
        <line x1="414" y1="517" x2="428" y2="517"/><line x1="414" y1="521" x2="426" y2="521"/>
        <line x1="416" y1="526" x2="416" y2="537"/><line x1="424" y1="526" x2="424" y2="537"/>
      </g>
      <rect x="18" y="673" width="16" height="30" rx="3" fill="none" stroke="#fff" stroke-width="3"/>
      <rect x="22" y="697" width="8" height="3" fill="#fff"/>
      <rect x="300" y="666" width="11" height="8" fill="var(--red)"/>
      <polyline points="300,666 305.5,671 311,666" fill="none" stroke="#101010" stroke-width="1"/>
      <circle cx="305.5" cy="698" r="5.5" fill="none" stroke="var(--red)" stroke-width="1.2"/>
      <line x1="300" y1="698" x2="311" y2="698" stroke="var(--red)" stroke-width="1"/>
      <ellipse cx="305.5" cy="698" rx="2.3" ry="5.5" fill="none" stroke="var(--red)" stroke-width="1"/>
    </svg>

    <div class="brand" style="top:28px">
      <span class="brand-dot" style="width:30px;height:30px"></span>
      <div class="brand-name" style="font-size:21px;line-height:21px;margin-top:14px">Sentinel Ridge</div>
      <div class="brand-sub" style="font-size:7.2px;letter-spacing:4px;margin-top:2px">CONSULTING SERVICES</div>
      <div class="brand-tag" style="font-size:5.2px;letter-spacing:2.4px;margin-top:4px">commitment - integrity - results</div>
    </div>

    <h2 class="section-title" style="top:146px"><span class="accent">ABOUT</span> US</h2>
    <div class="rule" style="top:170px"></div>
    <div class="copy-block" style="top:180px;width:462px">
      <p class="copy">Lorem Ipsum is simply dummy text of the printing and typesetting industry. Lorem Ipsum has been the industry's standard dummy text ever since the 1500s, when an unknown printer took a galley of type and scrambled it to make a type specimen book. It has survived not only five centuries, but also the leap into electronic typesetting, remaining essentially unchanged.</p>
      <p class="copy">Lorem Ipsum is simply dummy text of the printing and typesetting industry. Lorem Ipsum has been the industry's standard dummy text ever since the 1500s,</p>
    </div>

    <h2 class="section-title" style="top:309px"><span class="accent">WHY</span> CHOOSE US</h2>
    <div class="rule" style="top:339px"></div>
    <p class="copy copy--abs" style="top:354px;width:250px">Lorem Ipsum is simply dummy text of the printing and typesetting industry. Lorem Ipsum has been the industry's standard dummy text ever since the 1500s, when an unknown printer took a galley of type and scrambled it to make a type specimen book. It has survived not only five centuries, but also the leap into electronic typesetting, remaining essentially unchanged.</p>

    <div class="service" style="left:22px;top:555px">
      <div class="service-title">NATIONAL<br>SECURITY</div>
      <div class="service-text">Morbi diam mauris viverra in gravida eu mattis in an</div>
    </div>
    <div class="service" style="left:188px;top:555px">
      <div class="service-title">RISK MANAGEMENT<br>SERVICES</div>
      <div class="service-text">Morbi diam mauris viverra in gravida eu mattis in an</div>
    </div>
    <div class="service service--blue" style="left:354px;top:555px">
      <div class="service-title">CONSULTING<br>SERVICES</div>
      <div class="service-text">Morbi diam mauris viverra in gravida eu mattis in an</div>
    </div>

    <div class="footer">
      <div class="footer-call">For More Information, Call Us Today!</div>
      <div class="footer-phone">0123.456.789</div>
      <div class="footer-contact" style="top:12px">info@yourmailid.com</div>
      <div class="footer-contact" style="top:34px">www.yourwebsite.com</div>
    </div>
  </section>

  <div class="sheet-label" style="left:66px">FRONT</div>
  <div class="sheet-label" style="left:630px">BACK</div>
</div>
</body>
</html>
```